corvane business cards

Hey design gurus!
I'm after a clean, modern, stylish business card for my about to be launched company.
I've uploaded the logos for my company "Corvane Electrical Solutions"
and also the brightway electricians logo to whom i am associated.

```html
<!DOCTYPE html>
<html lang="en">
<head>
<meta charset="utf-8">
<title>Corvane Electrical Solutions — Business Cards</title>
<link rel="stylesheet" href="https://fonts.googleapis.com/css2?family=Source+Sans+3:wght@400;600;700&display=swap">
<style>
  :root {
    --backdrop: #1a1a1a;
    --card-dark: #050505;
    --card-light: #9a9a9a;
    --brand-blue: #1e8fe6;
    --link-blue: #2c8fe0;
    --white: #ffffff;
    --badge-fill: #d9d9d9;
  }
  * { margin: 0; padding: 0; box-sizing: border-box; }
  html, body { width: 1200px; height: 800px; overflow: hidden; }
  body {
    background: var(--backdrop);
    font-family: "Source Sans 3", Arial, sans-serif;
    color: var(--white);
    position: relative;
  }
  .card {
    position: absolute;
    top: 174px;
    width: 291px;
    height: 451px;
    overflow: hidden;
    background:
      linear-gradient(160deg, var(--card-dark) 0%, #0b0b0b 55%, #2e2e2e 70%, var(--card-light) 100%);
    box-shadow: 0 10px 30px rgba(0,0,0,.5);
  }
  .card--front { left: 279px; }
  .card--back { left: 630px; }

  /* Front card */
  .front-name {
    position: absolute;
    left: 104px;
    top: 402px;
    transform-origin: 0 0;
    transform: rotate(-90deg);
    white-space: nowrap;
    font-weight: 700;
    color: var(--white);
  }
  .front-name__main { display: block; font-size: 58px; line-height: 44px; letter-spacing: 10px; text-transform: uppercase; }
  .front-name__sub { display: block; font-size: 17px; line-height: 20px; letter-spacing: 4.6px; text-transform: uppercase; margin-top: 6px; }

  .cord {
    position: absolute;
    left: 186px;
    width: 46px;
    background: linear-gradient(180deg, rgba(255,255,255,0), rgba(255,255,255,.35));
    border-radius: 4px;
  }
  .cord--top { top: 0; height: 66px; }
  .cord--bottom { top: 390px; height: 61px; background: linear-gradient(180deg, rgba(255,255,255,.35), rgba(255,255,255,.05)); }

  .tagline-bar {
    position: absolute;
    left: 197px;
    top: 70px;
    width: 24px;
    height: 316px;
    background: var(--white);
  }
  .tagline-bar__text {
    position: absolute;
    left: 2px;
    top: 313px;
    width: 310px;
    transform-origin: 0 0;
    transform: rotate(-90deg);
    text-align: center;
    color: var(--brand-blue);
    font-weight: 700;
    font-size: 18px;
    line-height: 20px;
    white-space: nowrap;
  }

  /* Back card */
  .back-name {
    position: absolute;
    top: 28px;
    left: 0;
    width: 291px;
    text-align: center;
    font-weight: 700;
    text-transform: uppercase;
  }
  .back-name__main { display: block; font-size: 36px; line-height: 34px; letter-spacing: 12px; margin-right: -12px; color: var(--brand-blue); }
  .back-name__sub { display: block; font-size: 12px; line-height: 16px; letter-spacing: 4.6px; margin-right: -4.6px; margin-top: 2px; color: var(--white); }

  .person {
    position: absolute;
    right: 29px;
    top: 144px;
    text-align: right;
  }
  .person__name { font-size: 16px; font-weight: 700; color: var(--brand-blue); line-height: 18px; }
  .person__role { font-size: 12px; line-height: 16px; margin-top: 2px; }
  .person__rule { width: 73px; height: 2px; background: var(--white); margin: 12px 0 0 auto; }

  .contact {
    position: absolute;
    right: 29px;
    top: 235px;
    text-align: right;
    font-size: 11px;
    line-height: 15px;
    list-style: none;
  }
  .contact__link { color: var(--link-blue); }

  .mark {
    position: absolute;
    left: 26px;
    top: 294px;
    display: flex;
    align-items: center;
  }
  .mark__circle {
    width: 134px; height: 134px;
    border-radius: 50%;
    border: 5px solid var(--brand-blue);
    display: flex; align-items: center; justify-content: center;
  }
  .mark__label {
    font-size: 20px; font-weight: 700; color: var(--white);
    letter-spacing: 1px; text-transform: uppercase;
  }
  .partner-badge {
    position: absolute;
    left: 158px;
    top: 392px;
    width: 120px;
    height: 41px;
    background: var(--badge-fill);
    border-radius: 4px;
  }
</style>
</head>
<body>
  <section class="card card--front" aria-label="Business card front">
    <div class="cord cord--top" role="img" aria-label="Illustration of a power cord and plug"></div>
    <h1 class="front-name">
      <span class="front-name__main">Corvane</span>
      <span class="front-name__sub">Electrical Solutions</span>
    </h1>
    <div class="tagline-bar">
      <p class="tagline-bar__text">NO DELAYS. NO MESS. NO EXCUSES</p>
    </div>
    <div class="cord cord--bottom" role="img" aria-label="Illustration of a power cord end"></div>
  </section>

  <section class="card card--back" aria-label="Business card back">
    <h2 class="back-name">
      <span class="back-name__main">Corvane</span>
      <span class="back-name__sub">Electrical Solutions</span>
    </h2>
    <div class="person">
      <p class="person__name">NAME IN HERE</p>
      <p class="person__role">Master Electrician/ CEO</p>
      <div class="person__rule"></div>
    </div>
    <ul class="contact">
      <li>Cell (555) 014-2738</li>
      <li>hello@corvane.co</li>
      <li class="contact__link">Corvane Electrical</li>
      <li class="contact__link">Solutions .com</li>
    </ul>
    <div class="mark">
      <div class="mark__circle"><span class="mark__label">Corvane</span></div>
    </div>
    <div class="partner-badge" role="img" aria-label="Brightway Electricians partner badge"></div>
  </section>
</body>
</html>
```